Korvel Reefworks business card

We sell live saltwater fish and live corals
Korvel Reefworks
7 Halden Ct
Brantmoor, NJ. 08147
(856) 319-7264
Contact Information for Business Card
Korvel Reefworks
7 Halden Ct
Brantmoor, NJ. 08147
(856) 319-7264
Colors
Designer to choose colors to be used in the design.

```html
<!DOCTYPE html>
<html lang="en">
<head>
<meta charset="utf-8">
<title>Korvel Reefworks – Business Card</title>
<link rel="stylesheet" href="https://fonts.googleapis.com/css2?family=Montserrat:wght@600;700&family=Open+Sans:wght@400;600&display=swap">
<style>
  :root {
    --page-bg: #e4e6e8;
    --card-white: #ffffff;
    --teal-light: #2fc3cc;
    --teal: #17a99f;
    --teal-text: #14a39a;
    --ocean-blue: #2d4fa6;
    --ink: #2a2a2a;
    --ink-soft: #4a4a4a;
    --mark-tint: rgba(255, 255, 255, 0.16);
  }
  * { margin: 0; padding: 0; box-sizing: border-box; }
  html, body {
    width: 1200px;
    height: 800px;
    overflow: hidden;
    background: var(--page-bg);
  }
  .canvas {
    position: relative;
    width: 1200px;
    height: 800px;
  }
  .card {
    position: absolute;
    width: 560px;
    height: 320px;
    box-shadow: 0 6px 18px rgba(0, 0, 0, 0.18);
    overflow: hidden;
  }

  /* Front face */
  .card-front {
    left: 390px;
    top: 50px;
    background: linear-gradient(180deg, var(--teal-light) 0%, var(--teal) 45%, var(--ocean-blue) 100%);
  }
  .front-name {
    position: absolute;
    left: 40px;
    top: 168px;
    font-family: "Montserrat", sans-serif;
    font-weight: 700;
    font-size: 34px;
    line-height: 1.05;
    color: var(--card-white);
    letter-spacing: 0.5px;
  }
  .front-mark-area {
    position: absolute;
    left: 330px;
    top: 60px;
    width: 210px;
    height: 210px;
    border-radius: 50%;
    background: var(--mark-tint);
  }

  /* Back face */
  .card-back {
    left: 250px;
    top: 420px;
    background: var(--card-white);
  }
  .brand {
    position: absolute;
    left: 34px;
    top: 128px;
    display: flex;
    align-items: center;
    gap: 12px;
  }
  .brand-dot {
    width: 46px;
    height: 46px;
    border-radius: 50%;
    background: var(--teal-light);
    flex: none;
  }
  .brand-name {
    font-family: "Montserrat", sans-serif;
    font-weight: 700;
    font-size: 25px;
    line-height: 1.05;
    color: var(--teal-text);
  }
  .divider {
    position: absolute;
    left: 262px;
    top: 70px;
    width: 2px;
    height: 180px;
    background: var(--teal-light);
  }
  .contact {
    position: absolute;
    left: 290px;
    top: 78px;
    font-family: "Open Sans", sans-serif;
    color: var(--ink);
  }
  .contact-name {
    font-family: "Montserrat", sans-serif;
    font-weight: 600;
    font-size: 20px;
    color: var(--teal-text);
  }
  .contact-role {
    font-size: 14px;
    color: var(--ink-soft);
    margin-bottom: 14px;
  }
  .contact-line {
    display: flex;
    align-items: center;
    gap: 6px;
    font-size: 14.5px;
    line-height: 1.4;
    white-space: nowrap;
  }
  .contact-line svg {
    width: 13px;
    height: 13px;
    flex: none;
  }
</style>
</head>
<body>
<main class="canvas">

  <section class="card card-front" aria-label="Card front">
    <div class="front-name">Korvel<br>Reefworks</div>
    <div class="front-mark-area"></div>
  </section>

  <section class="card card-back" aria-label="Card back">
    <div class="brand">
      <span class="brand-dot"></span>
      <span class="brand-name">Korvel<br>Reefworks</span>
    </div>
    <div class="divider"></div>
    <div class="contact">
      <div class="contact-name">Dorian Vale</div>
      <div class="contact-role">Owner</div>
      <div class="contact-line">7 Halden Ct</div>
      <div class="contact-line">Brantmoor, NJ. 08147</div>
      <div class="contact-line">
        <svg viewBox="0 0 16 16" aria-hidden="true"><path fill="#14a39a" d="M3.6 1.5l2.3 2.6-1.2 1.7c.9 2 2.5 3.6 4.5 4.5l1.7-1.2 2.6 2.3-1.3 2.3C7 13.3 2.7 9 1.3 2.8z"/></svg>
        (856) 319-7264
      </div>
      <div class="contact-line">
        <svg viewBox="0 0 16 16" aria-hidden="true"><rect x="1.5" y="3.5" width="13" height="9" fill="none" stroke="#14a39a" stroke-width="1.5"/><path d="M1.5 3.5L8 9l6.5-5.5" fill="none" stroke="#14a39a" stroke-width="1.5"/></svg>
        dorian@korvelreefworks.com
      </div>
      <div class="contact-line">
        <svg viewBox="0 0 16 16" aria-hidden="true"><circle cx="8" cy="8" r="6.3" fill="none" stroke="#14a39a" stroke-width="1.4"/><ellipse cx="8" cy="8" rx="2.8" ry="6.3" fill="none" stroke="#14a39a" stroke-width="1.2"/><path d="M1.8 8h12.4" stroke="#14a39a" stroke-width="1.2"/></svg>
        www.korvelreefworks.com
      </div>
    </div>
  </section>

</main>
</body>
</html>
```